Web Design For Metal Recycling Company

We are a scrap and recycling company dealing mainly in scrap metal base in Singapore. We deal in both domestic market and international market. Currently we are still unsure if we want to have a "lively" or "professional" company image so we will leave it to the designer to deem what is good.

We wish for a website to be able to "Retain" the interest of new visitor and at the same time able to give enough information for new and existing customer. We would also wish for design that will get the visitor to "Engage" us.

The attached is the logo for the company and we would want to incorporate that into the website. Either of the logo is fine.

```html
<!DOCTYPE html>
<html lang="en">
<head>
<meta charset="utf-8">
<title>Tai Hong Recycling</title>
<link rel="stylesheet" href="https://fonts.googleapis.com/css2?family=Michroma&family=Open+Sans:wght@400;600;700&display=swap">
<style>
:root{
  --gold:#d19a2a;
  --gold-light:#e4b64a;
  --grey:#7a7a7a;
  --text:#6d6d6d;
  --page:#f4f4f4;
  --band:#e8d5a8;
  --footer:#121212;
  --field:#2a2a2a;
  --white:#ffffff;
}
*{margin:0;padding:0;box-sizing:border-box}
html,body{width:1200px;height:1029px;overflow:hidden;background:var(--page)}
body{position:relative;font-family:"Open Sans",Arial,sans-serif;color:var(--text)}
.site{position:relative;width:1200px;height:1029px;overflow:hidden}
.abs{position:absolute}
.display{font-family:"Michroma","Arial",sans-serif;text-transform:uppercase}

/* header */
.top-rule{left:0;top:0;width:1200px;height:3px;background:var(--gold)}
.header{left:0;top:3px;width:1200px;height:87px;background:#f7f7f7}
.brand{left:172px;top:21px;display:flex;align-items:center;gap:12px}
.brand-square{width:50px;height:50px;border:3px solid var(--gold)}
.brand-name{font-family:"Michroma",sans-serif;font-size:21px;color:var(--gold);letter-spacing:1px;text-transform:uppercase}
.support{right:172px;top:19px;text-align:right}
.support-label{font-family:"Michroma",sans-serif;font-size:9px;color:var(--gold);text-transform:uppercase;letter-spacing:.5px}
.support-phone{font-size:15px;color:var(--grey);letter-spacing:1px;margin-top:-2px}
.support-icon{right:172px;top:17px}
.nav{left:673px;top:60px;display:flex;gap:3px}
.nav a{display:block;height:28px;padding:0 12px;font-family:"Michroma",sans-serif;font-size:8.5px;color:#8a8a8a;text-decoration:none;text-transform:uppercase;border-bottom:2px solid #d8d8d8;line-height:16px}
.nav a.active{color:var(--gold);border-bottom-color:var(--gold)}

/* hero */
.hero{left:0;top:90px;width:1200px;height:288px;background:linear-gradient(110deg,#c9c2b8 0%,#b96a3b 22%,#e07a3a 45%,#a8441c 70%,#d8803e 100%)}
.hero-arrow{top:118px;width:50px;height:50px;border-radius:50%;background:rgba(255,255,255,.35)}
.hero-arrow.prev{left:105px}
.hero-arrow.next{left:1045px}
.hero-arrow svg{position:absolute;left:15px;top:13px}
.hero-copy{left:540px;top:78px;width:500px;color:var(--white);font-size:19px;line-height:34px;letter-spacing:1px}
.hero-copy .accent{color:#e9d680;font-size:27px}
.dots{left:541px;top:220px;display:flex;gap:3px}
.dots span{width:7px;height:7px;background:rgba(255,255,255,.55)}
.dots span.on{background:var(--gold);outline:1px solid #fff}

/* welcome */
.welcome{left:0;top:378px;width:1200px;height:194px;text-align:center}
.welcome h1{margin-top:50px;font-family:"Michroma",sans-serif;font-size:14px;color:var(--gold);font-weight:400;letter-spacing:1px}
.welcome p{width:800px;margin:12px auto 0;font-size:14.5px;line-height:17px;color:#7b7b7b}

/* feature band */
.band{left:0;top:572px;width:1200px;height:183px;background:var(--band)}
.card{top:28px;height:130px;overflow:hidden}
.card .photo{position:absolute;inset:0}
.card .panel{position:absolute;left:0;top:0;width:137px;height:130px;background:rgba(20,14,10,.55);padding:20px 0 0 17px}
.card h2{font-family:"Michroma",sans-serif;font-size:14px;font-weight:400;color:var(--white)}
.card p{font-size:10px;line-height:12px;color:#eee;margin-top:5px;width:115px}
.card .more{position:absolute;left:17px;top:90px;display:flex;height:16px;background:var(--white);font-size:8px;font-weight:700;color:#333}
.card .more span{padding:0 8px;line-height:16px}
.card .more span+span{border-left:1px solid #ccc;padding:0 5px}
.card.scrap{left:192px;width:265px}
.card.recycle{left:469px;width:262px;box-shadow:0 0 0 2px #c9a24a}
.card.recycle h2{color:var(--gold-light)}
.card.recycle p{color:#c9a24a}
.card.recycle .more{background:var(--gold);color:#222}
.card.contact{left:742px;width:263px}

/* footer */
.footer{left:0;top:755px;width:1200px;height:274px;background:var(--footer)}
.footer h3{position:absolute;top:42px;font-family:"Michroma",sans-serif;font-size:13px;font-weight:400;color:#8a8a8a;text-transform:uppercase}
.field{position:absolute;left:173px;width:272px;background:var(--field);font-size:10px;color:#8a8a8a;padding:10px 12px}
.send{position:absolute;left:173px;top:201px;display:flex;height:24px;background:#555;font-size:10px;font-weight:700;color:#ccc}
.send span{line-height:24px;padding:0 19px}
.send span+span{border-left:1px solid #333;padding:0 9px;background:#444}
.map{position:absolute;left:468px;top:72px;width:272px;height:152px;border:3px solid #9a9a9a;background:linear-gradient(135deg,#e6e2d8,#d7d2c4)}
.foot-brand{position:absolute;left:762px;top:71px;display:flex;align-items:center;gap:8px}
.foot-brand .sq{width:30px;height:30px;border:2px solid var(--gold)}
.foot-brand .name{font-family:"Michroma",sans-serif;font-size:13px;color:var(--gold);text-transform:uppercase}
.copyright{position:absolute;left:762px;top:108px;width:240px;font-size:10px;line-height:14px;color:#8a8a8a}
.social{position:absolute;left:762px;top:143px;display:flex;gap:8px}
.social span{width:30px;height:30px;border-radius:50%;background:#3a3a3a;border:2px dashed #555;display:flex;align-items:center;justify-content:center}
.social span.on{background:#f4f0e4;border-color:var(--gold)}
</style>
</head>
<body>
<div class="site">
  <div class="abs top-rule"></div>
  <header class="abs header">
    <div class="abs brand">
      <div class="brand-square"></div>
      <div class="brand-name">Tai Hong Recycling</div>
    </div>
    <div class="abs support" style="right:195px">
      <div class="support-label">Customer support:</div>
      <div class="support-phone">+ 65 6100 2200</div>
    </div>
    <svg class="abs support-icon" width="18" height="22" viewBox="0 0 18 22" aria-hidden="true">
      <path d="M9 2a7 7 0 0 0-7 7v4h3V9a4 4 0 0 1 8 0v4h3V9a7 7 0 0 0-7-7z" fill="#333"/>
      <rect x="2" y="12" width="3" height="6" rx="1" fill="#333"/>
      <rect x="13" y="12" width="3" height="6" rx="1" fill="#333"/>
    </svg>
    <nav class="abs nav" style="top:57px">
      <a class="active" href="#">Home</a>
      <a href="#">About us</a>
      <a href="#">Product &amp; Services</a>
      <a href="#">Contact us</a>
    </nav>
  </header>

  <section class="abs hero" role="img" aria-label="Close-up photograph of coiled copper scrap">
    <div class="abs hero-arrow prev"><svg width="18" height="24"><path d="M13 2 4 12l9 10" stroke="#555" stroke-width="1.5" fill="none"/></svg></div>
    <div class="abs hero-arrow next"><svg width="18" height="24"><path d="M5 2l9 10-9 10" stroke="#555" stroke-width="1.5" fill="none"/></svg></div>
    <div class="abs hero-copy display">We are a <span class="accent">Scrap</span> and <span class="accent">Recycling</span> company dealing mainly in scrap metal base in Singapore.</div>
    <div class="abs dots"><span></span><span></span><span></span><span class="on"></span><span></span><span></span></div>
  </section>

  <section class="abs welcome">
    <h1>WELCOME</h1>
    <p>Tai Hong, your One Stop Solution to all your scrap ferrous, Non-Ferrous and other recyclable.Tai Hong Hardware provides a one stop solution for procurement, recycling and trading of ferrous and non-ferrous scrap metal products for industries and individual.<br>With more than 30 years of experience in the industry, we know your needs.</p>
  </section>

  <section class="abs band">
    <article class="abs card scrap">
      <div class="photo" role="img" aria-label="Photograph of tangled copper wire scrap" style="background:linear-gradient(120deg,#3a2418,#7a4a2e 50%,#4a2d1c)"></div>
      <div class="panel">
        <h2>SCRAP</h2>
        <p>Duis autem vel eum iriure dolor in hendrerit in vulputate...</p>
      </div>
      <div class="more"><span>Read More</span><span>+</span></div>
    </article>
    <article class="abs card recycle">
      <div class="photo" role="img" aria-label="Photograph of cut cable ends showing copper cores" style="background:linear-gradient(120deg,#1c1c1c,#4a4a44 45%,#6a5a44 70%,#2a2a2a)"></div>
      <div class="panel" style="top:10px;height:120px;padding-top:12px">
        <h2>RECYCLING</h2>
        <p>Lorem ipsum dolor sit amet, consectetuer adipiscing eli...</p>
      </div>
      <div class="more" style="top:92px"><span>Read More</span><span>+</span></div>
    </article>
    <article class="abs card contact">
      <div class="photo" role="img" aria-label="Photograph of a recycling bin on a dark background" style="background:linear-gradient(120deg,#1e1e1e,#3a3a3a 55%,#6a6a6a 80%,#2a2a2a)"></div>
      <div class="panel">
        <h2>CONTACT</h2>
        <p>Ut wisi enim ad minim veniam, quis nostrud exerci tation ...</p>
      </div>
      <div class="more"><span>Read More</span><span>+</span></div>
    </article>
  </section>

  <footer class="abs footer">
    <h3 style="left:173px">Contact form</h3>
    <div class="field" style="top:72px;height:31px">Name*</div>
    <div class="field" style="top:108px;height:30px">Email*</div>
    <div class="field" style="top:143px;height:58px">Message*</div>
    <div class="send"><span>SEND</span><span>&gt;</span></div>

    <h3 style="left:468px">Map</h3>
    <div class="map" role="img" aria-label="Street map showing the company location"></div>

    <div class="foot-brand"><div class="sq"></div><div class="name">Tai Hong Recycling</div></div>
    <p class="copyright">© Copyright 2014 Tai Hong Hardware. All rights reserved.</p>
    <div class="social">
      <span class="on"></span>
      <span><svg width="14" height="10" viewBox="0 0 14 10"><rect x="0.5" y="0.5" width="13" height="9" fill="#bbb"/><path d="M.5.5 7 6l6.5-5.5" stroke="#3a3a3a" fill="none"/></svg></span>
      <span></span>
      <span></span>
    </div>
  </footer>
</div>
</body>
</html>
```